ROLLER SKATING RINK 5" Round Flyer

We are a skating rink in Miami Fl. This flyer will be used as our Fall Schedule. I have drawn up a sketch of what we are looking to do. We will work out wording and font styles later. I have all the copy needed for the flyer. I am open to your thoughts on the design if you have any to offer.

Target Market(s)

Kids from 8 years old to Adults.

Colors

Designer to choose colors to be used in the design.

Requirements
Must have
• Our company logo placed in the middle. I have this file and will send to anyone who needs it.
• READABILITY - CREATIVITY - FUN
Nice to have
• Colors that make you think MIAMI.
Should not have
• keep it PG, please. =)

```html
<!DOCTYPE html>
<html lang="en">
<head>
<meta charset="utf-8">
<title>Glide Loop Skating Center – Fall Schedule Flyer</title>
<link rel="stylesheet" href="https://fonts.googleapis.com/css2?family=Limelight&family=Poiret+One&display=swap">
<style>
  :root {
    --teal: #4f7d71;
    --yellow: #f9d65e;
    --butter: #fbec9e;
    --mint: #b9f1d6;
    --pink: #f5c7bd;
    --paper: #ffffff;
    --deco: "Limelight", "Poiret One", cursive;
    --light: "Poiret One", "Limelight", cursive;
  }
  html, body { margin: 0; padding: 0; overflow: hidden; background: var(--paper); }
  .flyer { position: relative; width: 1181px; height: 1200px; overflow: hidden; background: var(--paper); }
  .flyer__art { position: absolute; inset: 0; }

  .label { position: absolute; transform: translate(-50%, -50%); margin: 0; white-space: nowrap; text-align: center; line-height: 1.05; }

  .coupon { font-family: var(--deco); font-size: 40px; letter-spacing: 1px; }
  .coupon--light { font-family: var(--light); font-weight: 400; }
  .coupon--mint { color: var(--mint); text-shadow: 2px 2px 0 #8fd8b6; }
  .coupon--yellow { color: var(--butter); text-shadow: 2px 2px 0 var(--yellow); }
  .coupon--pink { color: var(--pink); text-shadow: 2px 2px 0 #e7a89b; }
  .coupon--teal { color: var(--teal); text-shadow: 2px 2px 0 var(--mint); }

  .badge-party { font-family: var(--deco); font-size: 46px; color: var(--teal); text-shadow: 4px 4px 0 var(--mint); transform: translate(-50%, -50%) rotate(-20deg); line-height: 1; }
  .badge-book { font-family: var(--deco); font-size: 56px; color: var(--yellow); -webkit-text-stroke: 1.5px var(--teal); text-shadow: 5px 4px 0 var(--mint); transform: translate(-50%, -50%) rotate(14deg); line-height: 0.95; }

  .packages { position: absolute; left: 806px; top: 478px; margin: 0; padding: 0; list-style: none; }
  .packages__item { display: flex; align-items: center; height: 60px; font-family: var(--deco); font-size: 34px; color: var(--yellow); text-shadow: -4px 2px 0 var(--mint); }
  .packages__star { width: 26px; height: 26px; margin-right: 10px; flex: none; }

  .brand { position: absolute; left: 595px; top: 599px; transform: translate(-50%, -50%); margin: 0; text-align: center; font-family: var(--deco); font-size: 50px; line-height: 1.05; color: var(--butter); }
  .brand__sub { display: block; font-size: 26px; letter-spacing: 2px; margin-top: 10px; }
</style>
</head>
<body>
<main class="flyer">
  <svg class="flyer__art" width="1181" height="1200" viewBox="0 0 1181 1200" aria-hidden="true">
    <defs>
      <clipPath id="disc"><circle cx="595" cy="599" r="551"/></clipPath>
      <g id="scissors" fill="none" stroke="var(--teal)" stroke-width="2">
        <circle cx="-8" cy="-6" r="4"/><circle cx="-8" cy="6" r="4"/>
        <line x1="-4" y1="-4" x2="14" y2="6"/><line x1="-4" y1="4" x2="14" y2="-6"/>
      </g>
    </defs>

    <!-- cut lines -->
    <g clip-path="url(#disc)" stroke="var(--teal)" stroke-width="2" stroke-dasharray="8 6">
      <line x1="595" y1="40" x2="595" y2="1160"/>
      <line x1="30" y1="207" x2="595" y2="207"/>
      <line x1="30" y1="363" x2="595" y2="363"/>
      <line x1="30" y1="520" x2="405" y2="520"/>
      <line x1="30" y1="677" x2="405" y2="677"/>
      <line x1="30" y1="835" x2="595" y2="835"/>
      <line x1="30" y1="991" x2="595" y2="991"/>
    </g>
    <use href="#scissors" x="228" y="196"/>
    <use href="#scissors" x="122" y="354"/>
    <use href="#scissors" x="70" y="510"/>
    <use href="#scissors" x="66" y="667"/>
    <use href="#scissors" x="108" y="824"/>
    <use href="#scissors" x="226" y="980"/>

    <!-- outer frame -->
    <circle cx="595" cy="599" r="555" fill="none" stroke="var(--teal)" stroke-width="9"/>
    <circle cx="1044" cy="211" r="5" fill="var(--teal)"/>

    <!-- party seal -->
    <circle cx="766" cy="268" r="138" fill="var(--butter)"/>
    <circle cx="766" cy="268" r="140" fill="none" stroke="var(--butter)" stroke-width="22" stroke-dasharray="0 27.5" stroke-linecap="round"/>

    <!-- booking octagon -->
    <polygon points="716,820 816,820 886,890 886,990 816,1060 716,1060 646,990 646,890" fill="var(--pink)"/>

    <!-- centre disc -->
    <circle cx="595" cy="599" r="198" fill="var(--teal)"/>
  </svg>

  <p class="label coupon coupon--mint" style="left:445px;top:141px">POINT<br>CUT SPECIAL</p>
  <p class="label coupon coupon--yellow" style="left:366px;top:284px">POINT CUT SPECIAL</p>
  <p class="label coupon coupon--pink" style="left:264px;top:445px">POINT CUT SPECIAL</p>
  <p class="label coupon coupon--yellow" style="left:220px;top:596px">POINT<br>CUT SPECIAL</p>
  <p class="label coupon coupon--light coupon--pink" style="left:264px;top:753px">POINT CUT SPECIAL</p>
  <p class="label coupon coupon--teal" style="left:366px;top:909px">POINT CUT SPECIAL</p>
  <p class="label coupon coupon--mint" style="left:467px;top:1048px">POINT<br>CUT SPECIAL</p>

  <p class="label badge-party" style="left:772px;top:262px">PUT YOUR<br>PARTY ON<br>WHEELS !</p>

  <h1 class="brand">GLIDE LOOP<span class="brand__sub">SKATING CENTER</span></h1>

  <ul class="packages">
    <li class="packages__item"><svg class="packages__star" viewBox="-13 -13 26 26"><polygon fill="var(--teal)" points="0,-12 3,-6 9,-9 7,-3 12,0 7,3 9,9 3,6 0,12 -3,6 -9,9 -7,3 -12,0 -7,-3 -9,-9 -3,-6"/></svg>STANTARD</li>
    <li class="packages__item"><svg class="packages__star" viewBox="-13 -13 26 26"><polygon fill="var(--teal)" points="0,-12 3,-6 9,-9 7,-3 12,0 7,3 9,9 3,6 0,12 -3,6 -9,9 -7,3 -12,0 -7,-3 -9,-9 -3,-6"/></svg>DELUXE</li>
    <li class="packages__item"><svg class="packages__star" viewBox="-13 -13 26 26"><polygon fill="var(--teal)" points="0,-12 3,-6 9,-9 7,-3 12,0 7,3 9,9 3,6 0,12 -3,6 -9,9 -7,3 -12,0 -7,-3 -9,-9 -3,-6"/></svg>SUPER</li>
    <li class="packages__item"><svg class="packages__star" viewBox="-13 -13 26 26"><polygon fill="var(--teal)" points="0,-12 3,-6 9,-9 7,-3 12,0 7,3 9,9 3,6 0,12 -3,6 -9,9 -7,3 -12,0 -7,-3 -9,-9 -3,-6"/></svg>SEMI-PRIVATE</li>
    <li class="packages__item"><svg class="packages__star" viewBox="-13 -13 26 26"><polygon fill="var(--teal)" points="0,-12 3,-6 9,-9 7,-3 12,0 7,3 9,9 3,6 0,12 -3,6 -9,9 -7,3 -12,0 -7,-3 -9,-9 -3,-6"/></svg>EXCLUSIVE</li>
  </ul>

  <p class="label badge-book" style="left:770px;top:938px">BOOK<br>ON LINE<br>NOW !</p>
</main>
</body>
</html>
```